Kestmar Conflict Varnok Legion Memoir Book Cover Design

We need a book cover design for a Russian kestmar conflict memoir.
Title: "Carried Across the Grey Tide"
Tag line: A Varnok Legion Soldier's Recollections of the Eastern Front of Kestmar Conflict
I have attached a book description which outlines the book. This is to go on the back cover.
I have attached images of book covers of the style we are looking for. Being Russia and War.
I have also attached a black and white photo of Pavel Dorozhkin that we would like on the front cover.
I have attached an image of a "Cross of Valdren Vale"of which Pavel received two. If an image of this could be incorporated on the front or back.
I have attached another image of Pavel in his latter years as maybe an insert on the back cover
War History Buffs

```html
<!DOCTYPE html>
<html lang="en">
<head>
<meta charset="utf-8">
<title>Carried Across the Grey Tide — Book Cover</title>
<link rel="stylesheet" href="https://fonts.googleapis.com/css2?family=Playfair+Display:ital,wght@0,400;0,700;0,800;1,400&display=swap">
<style>
  :root {
    --cover-red: #d40000;
    --cover-red-bright: #ff1a0f;
    --cover-red-deep: #c80000;
    --ink-white: #ffffff;
  }
  html, body {
    margin: 0;
    padding: 0;
    width: 846px;
    height: 1200px;
    overflow: hidden;
    background: var(--cover-red);
  }
  .cover {
    position: relative;
    width: 846px;
    height: 1200px;
    overflow: hidden;
    background: var(--cover-red);
    font-family: "Playfair Display", Georgia, serif;
    color: var(--ink-white);
  }
  .cover-artwork {
    position: absolute;
    inset: 0;
    background:
      radial-gradient(ellipse 38% 48% at 78% 52%, var(--cover-red-bright) 0%, rgba(255,26,15,0) 100%),
      radial-gradient(ellipse 30% 22% at 40% 30%, rgba(255,26,15,0.7) 0%, rgba(255,26,15,0) 100%),
      radial-gradient(ellipse 60% 18% at 50% 8%, rgba(255,20,10,0.55) 0%, rgba(255,20,10,0) 100%),
      linear-gradient(180deg, var(--cover-red) 0%, var(--cover-red-deep) 100%);
  }
  .cover-title {
    position: absolute;
    left: 86px;
    top: 372px;
    margin: 0;
    font-weight: 700;
    font-size: 138px;
    line-height: 131px;
    letter-spacing: -2px;
    text-transform: uppercase;
  }
  .cover-title span { display: block; }
  .cover-tagline {
    position: absolute;
    left: 88px;
    top: 936px;
    margin: 0;
    font-weight: 400;
    font-size: 37px;
    line-height: 47px;
    letter-spacing: -0.5px;
  }
  .cover-tagline span { display: block; }
  .cover-author {
    position: absolute;
    left: 88px;
    top: 1062px;
    margin: 0;
    font-style: italic;
    font-weight: 400;
    font-size: 30px;
    line-height: 40px;
  }
</style>
</head>
<body>
  <main class="cover">
    <div class="cover-artwork" role="img" aria-label="Red-toned collage of an Eastern Front campaign map overlaid with an onion-domed cathedral"></div>
    <h1 class="cover-title">
      <span>Carried</span>
      <span>Across</span>
      <span>the Grey</span>
      <span>Tide</span>
    </h1>
    <p class="cover-tagline">
      <span>A Varnok Legion Soldier’s Recollections</span>
      <span>of the Eastern Front of Kestmar Conflict</span>
    </p>
    <p class="cover-author">Pavel Semyonovich Dorozhkin</p>
  </main>
</body>
</html>
```